Pelk coffee cup design (paper and plastic cup)

Im looking for either a black or earth tones ( beige,tan,sand) cup design
Ultra modern and simple
Looking for ideas

Target Market(s)

College students, 16-30

Industry/Entity Type

Coffee

Font styles to use
Sans Serif

Colors

Designer to choose colors to be used in the design.

Requirements
Must have
• Modern design, minimalist (new york) under the logo
Nice to have
• I want there to be a little easter egg(small or hidden image of a buffalo)
Should not have
• busy design

```html
<!DOCTYPE html>
<html lang="en">
<head>
<meta charset="utf-8">
<title>Pelk Coffee – Cup Wrap</title>
<link href="https://fonts.googleapis.com/css2?family=Montserrat:wght@300;400&display=swap" rel="stylesheet">
<style>
  :root {
    --backdrop: #6b6747;
    --wrap-black: #0a0a0a;
    --olive-ink: #8c8458;
    --olive-soft: #6f6a45;
    --olive-deep: #3d3a25;
  }
  html, body {
    margin: 0;
    padding: 0;
    width: 1200px;
    height: 1200px;
    overflow: hidden;
    background: var(--backdrop);
  }
  .canvas {
    position: relative;
    width: 1200px;
    height: 1200px;
    background: var(--backdrop);
  }
  .cup-wrap {
    position: absolute;
    left: 330px;
    top: 150px;
    width: 540px;
    height: 900px;
    background: var(--wrap-black);
    font-family: "Montserrat", sans-serif;
    color: var(--olive-ink);
  }
  .brand {
    position: absolute;
    top: 215px;
    left: 0;
    width: 100%;
    text-align: center;
  }
  .brand-mark {
    display: block;
    width: 32px;
    height: 32px;
    margin: 0 auto 28px;
    border: 1.5px solid var(--olive-ink);
    box-sizing: border-box;
  }
  .brand-name {
    margin: 0;
    font-weight: 300;
    font-size: 24px;
    letter-spacing: 0.16em;
    padding-left: 0.16em;
  }
  .brand-est {
    margin: 18px 0 0;
    font-weight: 400;
    font-size: 12px;
    letter-spacing: 0.04em;
  }
  .buffalo-art {
    position: absolute;
    left: 105px;
    top: 570px;
    width: 330px;
    height: 270px;
  }
</style>
</head>
<body>
  <main class="canvas">
    <section class="cup-wrap">
      <header class="brand">
        <span class="brand-mark"></span>
        <h1 class="brand-name">PELK COFFEE</h1>
        <p class="brand-est">est. 2022</p>
      </header>
      <svg class="buffalo-art" viewBox="0 0 330 270" role="img" aria-label="Olive-toned illustration of a walking buffalo">
        <defs>
          <linearGradient id="buffaloTone" x1="0" y1="0" x2="0" y2="1">
            <stop offset="0" stop-color="var(--olive-soft)"/>
            <stop offset="1" stop-color="var(--olive-deep)"/>
          </linearGradient>
        </defs>
        <rect x="0" y="0" width="330" height="270" rx="40" fill="url(#buffaloTone)"/>
      </svg>
    </section>
  </main>
</body>
</html>
```